Business card for femtech company

Nothing too elaborate but elegant and geared towards the mother and baby market. Prefer full-bleed with logo (attached) rear.

```html
<!DOCTYPE html>
<html lang="en">
<head>
<meta charset="utf-8">
<title>nuvia business card</title>
<link href="https://fonts.googleapis.com/css2?family=Poppins:wght@400;500;600;700&display=swap" rel="stylesheet">
<style>
  :root {
    --backdrop: #8a8a8a;
    --teal: #5bc2ba;
    --teal-soft: #7ccac5;
    --teal-pale: #b2e2de;
    --white: #ffffff;
    --wordmark: #c4c4c4;
    --tagline: #f4a0a0;
  }
  * { margin: 0; padding: 0; box-sizing: border-box; }
  html, body { width: 1200px; height: 1000px; overflow: hidden; }
  body {
    background: var(--backdrop);
    font-family: "Poppins", sans-serif;
    position: relative;
  }
  .card {
    position: absolute;
    left: 294px;
    width: 613px;
    height: 352px;
    border-radius: 28px;
    overflow: hidden;
    box-shadow: 0 8px 24px rgba(0,0,0,0.22);
  }
  .card--front { top: 137px; background: var(--white); }
  .card--back { top: 542px; background: var(--teal); }
  .card__curve { position: absolute; inset: 0; width: 100%; height: 100%; }
  .brand {
    position: absolute;
    display: flex;
    align-items: center;
    gap: 10px;
  }
  .brand__dot {
    width: 50px; height: 50px;
    border-radius: 50%;
    background: var(--teal);
  }
  .brand__name {
    font-weight: 400;
    font-size: 52px;
    line-height: 1;
    color: var(--wordmark);
  }
  .card--front .brand { left: 46px; top: 60px; }
  .tagline {
    position: absolute;
    left: 44px; top: 117px;
    font-size: 18px;
    font-weight: 500;
    color: var(--tagline);
  }
  .card--back .brand { left: 372px; top: 262px; }
  .contact { position: absolute; left: 50px; top: 104px; color: var(--white); }
  .contact__name { font-size: 24px; font-weight: 600; line-height: 1.2; }
  .contact__role { font-size: 17px; font-weight: 700; line-height: 1.2; margin-bottom: 28px; }
  .contact__list { list-style: none; font-size: 16.5px; line-height: 21.5px; }
  .contact__list li { display: flex; align-items: center; gap: 5px; }
  .contact__list svg { width: 18px; height: 18px; flex: none; }
</style>
</head>
<body>

<section class="card card--front">
  <svg class="card__curve" viewBox="0 0 613 352" aria-hidden="true">
    <ellipse cx="600" cy="420" rx="378" ry="358" fill="var(--teal-pale)"/>
    <ellipse cx="606" cy="426" rx="356" ry="338" fill="var(--teal-soft)"/>
  </svg>
  <div class="brand">
    <span class="brand__dot"></span>
    <span class="brand__name">nuvia</span>
  </div>
  <p class="tagline">breastfeeding monitor</p>
</section>

<section class="card card--back">
  <svg class="card__curve" viewBox="0 0 613 352" aria-hidden="true">
    <ellipse cx="610" cy="420" rx="372" ry="370" fill="var(--teal-pale)"/>
    <ellipse cx="616" cy="426" rx="350" ry="350" fill="var(--white)"/>
  </svg>
  <div class="contact">
    <p class="contact__name">Name Surname</p>
    <p class="contact__role">Position</p>
    <ul class="contact__list">
      <li>
        <svg viewBox="0 0 24 24" aria-hidden="true"><path fill="#fff" d="M6.6 10.8a15.1 15.1 0 0 0 6.6 6.6l2.2-2.2c.3-.3.7-.4 1-.2 1.1.4 2.3.6 3.6.6.6 0 1 .4 1 1V20c0 .6-.4 1-1 1A17 17 0 0 1 3 4c0-.6.4-1 1-1h3.5c.6 0 1 .4 1 1 0 1.3.2 2.5.6 3.6.1.3 0 .7-.2 1z"/></svg>
        (123) 456-890
      </li>
      <li>
        <svg viewBox="0 0 24 24" aria-hidden="true"><rect x="2.5" y="5" width="19" height="14" rx="1.5" fill="none" stroke="#fff" stroke-width="1.8"/><path d="M3 6l9 7 9-7" fill="none" stroke="#fff" stroke-width="1.8"/></svg>
        info@nuviababy.com
      </li>
      <li>
        <svg viewBox="0 0 24 24" aria-hidden="true"><g fill="none" stroke="#fff" stroke-width="1.5"><circle cx="12" cy="12" r="9"/><ellipse cx="12" cy="12" rx="4" ry="9"/><path d="M3 12h18M4.5 7.5h15M4.5 16.5h15"/></g></svg>
        nuviababy.com
      </li>
    </ul>
  </div>
  <div class="brand">
    <span class="brand__dot"></span>
    <span class="brand__name">nuvia</span>
  </div>
</section>

</body>
</html>
```